Vemra. Packaging for mood-boosting energy drink mix. Upbeat and uplifting.

I need a mockup of a pouch package + a stick. I included an image of a Aqua Tarn pouch + stick for reference. I do not have a die line for the pouch, so feel free to just use the same relative dimensions for the pouch and create a rendering. Here are the specifications for the packaging that I need:
1. The logo is included in the uploaded files. Please use the one that says "bright day spark" beneath "vemra." The logo should take up about the top 1/3 to 1/2 of the pouch.
2. The pouch should be mostly white, especially behind the logo, but feel free to explore yellow or orange for the bottom 1/2 to 2/3 of the packaging.
3. In the center of the packaging, below the logo, please have the product name appear, "mood-boosting energy drink mix" similar to where "Fluid Amplifier" is placed.
4. Below that, create an image of a glass with a stick pouring into it like in the Aqua Tarn pouch.
5. Below the glass, in the bottom center of the package, include "16 sticks. Net Wt. 4 oz. (114 g)
6. On the left side, please include callouts, from top to bottom, "energy blend (80mg caffeine, taurine) + happy blend (saffron, st. john's wort, rhodiola).
7. On the right side, please include callouts, from top to bottom, "electrolytes + vitamins + 0g sugar"
8. Somewhere else on the front of the packaging, please include the flavor name "golden berry," perhaps where they do on the aqua tarn pouch.
9. For the stick, use your creativity.
10. There is no back of packaging to design for this project.

Target Market(s)

My target consumer leads a very active lifestyle and cares deeply about health & wellness.

Colors
0094D4
00A9DD
6FCCEA
C7EBF8
E9F6FB
FFC000
F8CF3A
FAE287
FDF2CF
FEFAEE
F0912C
F2A743
F7CA91
FBE8D2
FDF5EE
EE7325
F08F49
F5BC92
FAE3D3
FDF4ED

Requirements
Must have
• My packaging must make people feel good and maybe even smile when they see it. A brand that does this well is Penn. (www.pennvita-example.com)
Nice to have
• I like 60's Mod Design if you need some inspiration. The packaging should also convey a sense of levity. Like you'll float or dance through life after drinking this.

```html
<!DOCTYPE html>
<html lang="en">
<head>
<meta charset="utf-8">
<title>Vemra – Golden Berry pouch and stick</title>
<link rel="stylesheet" href="https://fonts.googleapis.com/css2?family=Outfit:wght@400;500;600;700;800&display=swap">
<style>
  :root {
    --backdrop: #DE7635;
    --pouch-white: #F7F7F6;
    --brand-orange: #EE7325;
    --flavor-orange: #F0912C;
    --ink: #0E0E0E;
    --body-ink: #1F1F1F;
    --pattern-orange: #E9773A;
    --pattern-peach: #F5BC92;
    --pattern-cream: #F3E4D3;
    --badge-white: #F4F4F4;
    --glass-blue: #2E8FD0;
    --glass-light: #9FD3EE;
  }
  * { margin: 0; padding: 0; box-sizing: border-box; }
  html, body { width: 1200px; height: 835px; overflow: hidden; }
  body {
    background: var(--backdrop);
    font-family: "Outfit", sans-serif;
    position: relative;
  }

  /* ---------- pouch ---------- */
  .pouch {
    position: absolute;
    left: 95px; top: 58px;
    width: 640px; height: 721px;
    background: var(--pouch-white);
    overflow: hidden;
  }
  .pouch .brand-name {
    position: absolute; left: 0; top: 18px; width: 640px;
    text-align: center;
    font-weight: 600; color: var(--brand-orange);
    font-size: 200px; line-height: 1; letter-spacing: -5px;
    white-space: nowrap;
  }
  .pouch .product-name {
    position: absolute; left: 0; width: 640px; top: 250px;
    text-align: center;
    font-weight: 800; font-size: 30px; color: var(--ink);
    letter-spacing: -0.3px; white-space: nowrap;
  }
  .pouch .flavor {
    position: absolute; left: 0; width: 640px; top: 295px;
    text-align: center; font-weight: 600; font-size: 33px;
    color: var(--flavor-orange); letter-spacing: 0.3px;
  }
  .pouch .callout {
    position: absolute; top: 342px;
    font-size: 17px; line-height: 22.5px; color: var(--body-ink);
    font-weight: 400;
  }
  .pouch .callout.left { left: 26px; }
  .pouch .callout.right { left: 352px; }
  .pouch .pattern {
    position: absolute; left: 0; top: 419px;
    width: 640px; height: 302px;
    background: linear-gradient(135deg, var(--pattern-peach) 0%, var(--pattern-orange) 35%, var(--pattern-cream) 60%, var(--pattern-orange) 100%);
  }
  .pouch .badge {
    position: absolute; left: 217px; top: 467px;
    width: 210px; height: 210px; border-radius: 50%;
    background: var(--badge-white);
  }
  .pouch .pour-art {
    position: absolute; left: 47px; top: 22px;
    width: 116px; height: 160px; border-radius: 8px;
    background: linear-gradient(180deg, var(--glass-light) 0%, var(--glass-blue) 70%);
  }
  .pouch .count {
    position: absolute; left: 0; width: 210px; top: 186px;
    text-align: center; font-size: 12px; line-height: 1; color: var(--body-ink);
  }
  .pouch .net-weight {
    position: absolute; left: 0; width: 210px; top: 199px;
    text-align: center; font-size: 6px; line-height: 1; color: #666;
  }

  /* ---------- stick ---------- */
  .stick {
    position: absolute; left: 845px; top: 158px;
    width: 114px; height: 606px;
    background: var(--pouch-white); overflow: hidden;
  }
  .stick .seal {
    position: absolute; left: 0; width: 114px; height: 12px;
    background: #ECECEA;
  }
  .stick .seal.top { top: 0; }
  .stick .seal.bottom { bottom: 0; background: #EFD9C6; }
  .stick .brand-name {
    position: absolute; left: 20px; top: 236px;
    white-space: nowrap; line-height: 1;
    transform: rotate(-90deg); transform-origin: left top;
    font-weight: 600; color: var(--brand-orange);
    font-size: 74px; letter-spacing: -2px;
  }
  .stick .product-name {
    position: absolute; left: 15px; top: 253px;
    font-weight: 700; font-size: 8px; line-height: 11px; color: var(--ink);
  }
  .stick .flavor {
    position: absolute; left: 15px; top: 280px;
    font-weight: 500; font-size: 10px; color: var(--flavor-orange);
  }
  .stick .pattern {
    position: absolute; left: 12px; top: 312px;
    width: 90px; height: 282px;
    background: linear-gradient(160deg, var(--pattern-orange) 0%, var(--pattern-peach) 40%, var(--pattern-orange) 70%, var(--pattern-cream) 100%);
  }
  .stick .callout {
    position: absolute; left: 15px;
    font-size: 7.2px; line-height: 10px; color: var(--body-ink);
  }
  .stick .callout.upper { top: 328px; }
  .stick .callout.lower { top: 386px; }
</style>
</head>
<body>

<section class="pouch">
  <p class="brand-name">vemra</p>

  <h1 class="product-name">MOOD- BOOSTING ENERGY DRINK MIX</h1>
  <p class="flavor">GOLDEN BERRY</p>

  <p class="callout left">Energy blend (80mg Caffeine, Taurine)<br>+ Happy Blend (Saffron,<br>St. John's Wort, Rhodiola)</p>
  <p class="callout right">Electrolytes + Vitamins + 0g Sugar</p>

  <div class="pattern" role="img" aria-label="Mod pattern of orange, peach and cream quarter circles"></div>

  <div class="badge">
    <div class="pour-art" role="img" aria-label="Illustration of two sticks pouring powder into a fizzing blue glass"></div>
    <p class="count">16 sticks</p>
    <p class="net-weight">Net Wt. 4 oz. (114 g)</p>
  </div>
</section>

<section class="stick">
  <div class="seal top"></div>
  <p class="brand-name">vemra</p>

  <p class="product-name">MOOD- BOOSTING<br>ENERGY DRINK MIX</p>
  <p class="flavor">GOLDEN BERRY</p>

  <div class="pattern" role="img" aria-label="Mod pattern of orange, peach and cream quarter circles"></div>
  <p class="callout upper">Energy blend (80mg<br>Caffeine, Taurine) +<br>Happy Blend (Saffron,<br>St. John's Wort, Rhodiola)</p>
  <p class="callout lower">Electrolytes + Vitamins<br>+ 0g Sugar</p>
  <div class="seal bottom"></div>
</section>

</body>
</html>
```